Construction business card

I need a new business card, they can connect with my logo, brand.
What we do is residential house , design and build
I like: Navy blue / black
I attached our logo, brand,
and, some idea for business card.

```html
<!DOCTYPE html>
<html lang="en">
<head>
<meta charset="utf-8">
<title>Larkfield Building Group – Business Card</title>
<link rel="stylesheet" href="https://fonts.googleapis.com/css2?family=Poppins:wght@300;400;500;600;700&display=swap">
<style>
  :root {
    --stage: #1f1f21;
    --card-blue: #0e7ec4;
    --card-blue-deep: #0b72b3;
    --ink-white: #ffffff;
    --card-w: 720px;
    --card-h: 412px;
  }
  * { box-sizing: border-box; margin: 0; padding: 0; }
  html, body {
    width: 1200px;
    height: 1200px;
    overflow: hidden;
    background: var(--stage);
    font-family: "Poppins", sans-serif;
  }
  .stage {
    width: 1200px;
    height: 1200px;
    display: flex;
    flex-direction: column;
    align-items: center;
    justify-content: center;
    gap: 56px;
  }
  .card {
    position: relative;
    width: var(--card-w);
    height: var(--card-h);
    background: var(--card-blue);
    color: var(--ink-white);
  }
  /* Front */
  .card--front {
    display: flex;
    align-items: center;
    justify-content: center;
  }
  .brand-name {
    font-weight: 700;
    font-size: 38px;
    letter-spacing: 1px;
    text-transform: uppercase;
    text-align: center;
    line-height: 1.15;
    color: var(--ink-white);
  }
  /* Back */
  .contact {
    position: absolute;
    left: 58px;
    top: 72px;
  }
  .person-name {
    font-weight: 600;
    font-size: 25px;
    letter-spacing: 1px;
    text-transform: uppercase;
    line-height: 1.1;
  }
  .person-role {
    font-weight: 400;
    font-size: 17px;
    line-height: 1.3;
  }
  .divider {
    width: 190px;
    height: 2px;
    background: var(--ink-white);
    margin: 14px 0 18px;
  }
  .address {
    font-size: 17px;
    font-weight: 400;
    line-height: 1.35;
    font-style: normal;
    margin-bottom: 14px;
  }
  .contact-list { list-style: none; }
  .contact-item {
    display: flex;
    align-items: center;
    gap: 10px;
    font-size: 17px;
    line-height: 1.55;
  }
  .contact-icon { width: 14px; height: 14px; flex: none; }
  .abn {
    margin-top: 14px;
    font-size: 21px;
    font-weight: 500;
    letter-spacing: 0.5px;
  }
  .brand-emboss {
    position: absolute;
    right: 40px;
    top: 130px;
    width: 300px;
    font-weight: 700;
    font-size: 34px;
    text-transform: uppercase;
    text-align: center;
    line-height: 1.15;
    color: var(--card-blue-deep);
  }
</style>
</head>
<body>
<main class="stage">
  <section class="card card--front" aria-label="Card front">
    <h1 class="brand-name">Larkfield<br>Building Group</h1>
  </section>

  <section class="card card--back" aria-label="Card back">
    <div class="contact">
      <p class="person-name">Daniel Reeves</p>
      <p class="person-role">CEO/Principal</p>
      <div class="divider"></div>
      <address class="address">48 Ashcombe St,<br>Bayside, VIC 3190</address>
      <ul class="contact-list">
        <li class="contact-item">
          <svg class="contact-icon" viewBox="0 0 14 14" aria-hidden="true"><rect x="2" y="2" width="10" height="10" fill="none" stroke="#fff" stroke-width="1.6"/></svg>
          0400 555 018
        </li>
        <li class="contact-item">
          <svg class="contact-icon" viewBox="0 0 14 14" aria-hidden="true"><rect x="1" y="3" width="12" height="8" fill="#fff"/><path d="M1 3 L7 8 L13 3" fill="none" stroke="#0e7ec4" stroke-width="1.2"/></svg>
          info@larkfieldbuilding.com.au
        </li>
        <li class="contact-item">
          <svg class="contact-icon" viewBox="0 0 14 14" aria-hidden="true"><circle cx="7" cy="7" r="6" fill="none" stroke="#fff" stroke-width="1.3"/><ellipse cx="7" cy="7" rx="2.6" ry="6" fill="none" stroke="#fff" stroke-width="1"/><path d="M1 7 H13" stroke="#fff" stroke-width="1"/></svg>
          www.larkfieldbuilding.com.au
        </li>
      </ul>
      <p class="abn">ABN: 12 345 678 901</p>
    </div>
    <p class="brand-emboss" aria-hidden="true">Larkfield<br>Building Group</p>
  </section>
</main>
</body>
</html>
```